依頼詳細
値段は入れず、『不安を安心に』『疑問を納得へ』『生活保護のご葬儀 自己負担0円』と言った文言を入れていただきたいです。
葬儀の流れの図も入れていただきたいです。
※添付ファイルを参照ください。
記載項目
電話番号のところは◯にしておいてください
サイズ
A4
ページ数
片面
希望イメージ
シンプル 複雑
単色 カラフル
暗い 明るい
日常 高級
遊び心 厳粛
未来的 伝統的
女性的 男性的
希望する色
赤系
納品ファイル
• 高解像度JPG (.jpg)
• イラストレーター形式 (.ai)
• フォトショップ形式 (.psd)
• PNG形式 (.png)
補足説明
■ 選んだ理由

シンプルで中身がわかりやすく気に入りました

■ 提案者全員のお礼・コメント

ありがとうございます!!また機会がありましたらお願い致します

```html
<!DOCTYPE html>
<html lang="ja">
<head>
<meta charset="utf-8">
<title>生活保護のご葬儀について</title>
<link href="https://fonts.googleapis.com/css2?family=Noto+Sans+JP:wght@400;500;700&display=swap" rel="stylesheet">
<style>
:root{
  --rose:#e8688a;
  --rose-deep:#d93a5e;
  --red:#c8283c;
  --pink-soft:#fbe3ea;
  --ink:#444;
  --ink-soft:#6a6a6a;
  --line:#d9d9d9;
  --paper:#ffffff;
}
*{margin:0;padding:0;box-sizing:border-box}
html,body{width:880px;height:1200px;overflow:hidden;background:var(--paper)}
body{font-family:"Noto Sans JP",sans-serif;color:var(--ink);position:relative}
.glow{position:absolute;left:0;top:0;width:880px;height:330px;
  background:radial-gradient(circle at 80% 35%,rgba(245,170,190,.45),rgba(255,255,255,0) 55%),
             radial-gradient(circle at 55% 10%,rgba(250,200,215,.35),rgba(255,255,255,0) 45%)}
.title{position:absolute;left:48px;top:52px;color:var(--rose);font-weight:700;font-size:50px;line-height:1.22;letter-spacing:2px}
.promise{position:absolute;left:588px;top:28px;width:262px;height:128px;background:var(--rose);color:#fff;
  text-align:center;font-weight:700;font-size:21px;line-height:1.6;padding-top:14px;letter-spacing:1px}
.intro{position:absolute;left:48px;top:190px;width:480px;font-size:14.5px;line-height:1.85;font-weight:500}
.target{position:absolute;left:62px;top:294px;width:760px;display:flex;align-items:center;gap:24px}
.target-label{width:170px;height:62px;background:var(--pink-soft);color:var(--rose-deep);font-weight:700;font-size:17px;
  display:flex;align-items:center;justify-content:center;border-radius:2px}
.target-list{list-style:none;font-size:15px;font-weight:700;color:var(--red);line-height:1.7}
.target-list li::before{content:"";display:inline-block;width:11px;height:11px;background:var(--red);margin-right:8px}
.flow{position:absolute;left:48px;top:388px;width:790px;list-style:none}
.step{display:flex;border-top:1px solid var(--line);min-height:83px;padding:12px 0}
.step:last-child{border-bottom:1px solid var(--line)}
.step-head{width:320px;display:flex;align-items:flex-start;gap:16px;padding-top:2px}
.step-num{width:26px;height:26px;background:var(--red);color:#fff;font-weight:700;font-size:15px;
  display:flex;align-items:center;justify-content:center;flex:none}
.step-name{font-size:18px;font-weight:700;color:var(--ink);line-height:26px}
.step-text{flex:1;font-size:11.5px;line-height:1.7;color:var(--ink-soft)}
.footer{position:absolute;left:48px;top:1088px;width:790px;display:flex;justify-content:space-between;align-items:center}
.org{display:flex;align-items:center;gap:14px}
.org-mark{width:52px;height:52px;border:2px solid #bbb;border-radius:50%}
.org-kind{font-size:13px;color:var(--ink-soft)}
.org-name{font-size:34px;font-weight:500;color:#666;line-height:1}
.contact{text-align:left}
.contact-lead{font-size:16px;font-weight:700}
.contact-row{display:flex;align-items:center;gap:16px;margin-top:4px;font-weight:700}
.hours{font-size:14px}
.phone{display:flex;align-items:center;gap:6px;font-size:26px;color:var(--ink)}
</style>
</head>
<body>
<div class="glow" role="img" aria-label="淡いピンクの水玉模様の背景"></div>

<h1 class="title">生活保護の<br>ご葬儀について</h1>

<div class="promise">不安を安心に<br>疑問を納得へ<br>自己負担０円</div>

<p class="intro">ルミナでは生活保護受給者の葬儀(火葬)を承ります。<br>生活保護受給者の方は市区町村福祉事務所・社会福祉課に葬祭扶助の申請をすることにより喪主様は自己負担なしで御葬儀(火葬式)を執り行うことができます。</p>

<div class="target">
  <div class="target-label">対象者</div>
  <ul class="target-list">
    <li>生活保護受給者がお亡くなりになった場合</li>
    <li>生活保護受給者が喪主となった場合</li>
  </ul>
</div>

<ol class="flow">
  <li class="step"><div class="step-head"><span class="step-num">1</span><span class="step-name">ご連絡</span></div>
    <p class="step-text">生活保護受給者がお亡くなりになった場合、弊社にご連絡ください。<br>24時間年中無休で受付しております。<br>お問い合わせ先　00-0000-0000</p></li>
  <li class="step"><div class="step-head"><span class="step-num">2</span><span class="step-name">お迎え</span></div>
    <p class="step-text">病院や施設、ご自宅など指定の場所へ寝台車でお迎えにあがります。</p></li>
  <li class="step"><div class="step-head"><span class="step-num">3</span><span class="step-name">ご安置・ご遺体安置</span></div>
    <p class="step-text">ご自宅または安置施設にてご遺体をお預かりし、<br>ドライアイス等で丁寧に保全いたします。</p></li>
  <li class="step"><div class="step-head"><span class="step-num">4</span><span class="step-name">お打合せ</span></div>
    <p class="step-text">■ 火葬日時・火葬場の確認<br>福祉事務所と連絡を取り、必要な手続きをご案内いたします。<br>■ 死亡届の提出<br>役所への届出は弊社が代行いたします。</p></li>
  <li class="step"><div class="step-head"><span class="step-num">5</span><span class="step-name">ご出棺・火葬</span></div>
    <p class="step-text">火葬当日、お別れの後にご出棺し火葬場へ向かいます。<br>ご親族の方も同行いただけます。</p></li>
  <li class="step"><div class="step-head"><span class="step-num">6</span><span class="step-name">荼毘</span></div>
    <p class="step-text">火葬場にて荼毘に付します。<br>待合室にてお待ちいただきます。</p></li>
  <li class="step"><div class="step-head"><span class="step-num">7</span><span class="step-name">ご収骨</span></div>
    <p class="step-text">ご遺骨を骨壺に納め、ご親族様へお渡しいたします。</p></li>
  <li class="step"><div class="step-head"><span class="step-num">8</span><span class="step-name">生活保護ご葬儀の申請</span></div>
    <p class="step-text">葬祭扶助の申請書類は弊社が福祉事務所へ提出いたします。<br>喪主様のご負担はございません。</p></li>
</ol>

<div class="footer">
  <div class="org">
    <span class="org-mark"></span>
    <div><div class="org-kind">一般社団法人</div><div class="org-name">Lumina</div></div>
  </div>
  <div class="contact">
    <div class="contact-lead">まずはお気軽にお電話ください。</div>
    <div class="contact-row">
      <span class="hours">24時間対応・年中無休</span>
      <span class="phone"><svg width="22" height="22" viewBox="0 0 24 24"><path fill="#444" d="M6.6 10.8a15.1 15.1 0 0 0 6.6 6.6l2.2-2.2a1 1 0 0 1 1-.25 11.4 11.4 0 0 0 3.6.57 1 1 0 0 1 1 1V20a1 1 0 0 1-1 1A17 17 0 0 1 3 4a1 1 0 0 1 1-1h3.5a1 1 0 0 1 1 1c0 1.25.2 2.45.57 3.57a1 1 0 0 1-.25 1z"/></svg>00-0000-0000</span>
    </div>
  </div>
</div>
</body>
</html>
```